Timber Ridge Land Services Business Cards

Need to create a business card with the company logo "Timber Ridge Land Services". The business will provide forestry mulching for land clearing and vegetation control, brush and small tree removal, wildlife habitat improvement and trail and property access creation.

```html
<!DOCTYPE html>
<html lang="en">
<head>
<meta charset="utf-8">
<title>Timber Ridge Land Services – Business Cards</title>
<link href="https://fonts.googleapis.com/css2?family=Jost:wght@400;500;700&display=swap" rel="stylesheet">
<style>
  :root {
    --page-bg: #e9ebea;
    --card-bg: #ffffff;
    --card-shade: #f1f3f2;
    --green-dark: #0f5a3a;
    --green-mid: #2f8a4c;
    --green-light: #7cc576;
    --text: #3a3f3c;
  }
  * { box-sizing: border-box; margin: 0; padding: 0; }
  html, body { width: 1200px; height: 900px; overflow: hidden; }
  body {
    background: var(--page-bg);
    font-family: "Jost", sans-serif;
    color: var(--text);
    display: flex;
    flex-direction: column;
    align-items: center;
    justify-content: center;
    gap: 56px;
  }
  .card {
    position: relative;
    width: 660px;
    height: 384px;
    border-radius: 28px;
    background: linear-gradient(160deg, var(--card-shade) 0%, var(--card-bg) 55%);
    box-shadow: 0 6px 18px rgba(0,0,0,0.12);
    overflow: hidden;
  }
  .brand {
    position: absolute;
    left: 52px;
    bottom: 56px;
    display: flex;
    align-items: center;
    gap: 12px;
  }
  .brand-mark {
    width: 16px; height: 16px;
    background: var(--green-light);
  }
  .brand-name {
    font-weight: 700;
    font-size: 24px;
    line-height: 1.1;
    color: var(--green-dark);
    text-transform: uppercase;
    letter-spacing: 0.5px;
    width: 270px;
  }
  .divider {
    position: absolute;
    left: 352px;
    bottom: 48px;
    width: 1.5px;
    height: 118px;
    background: var(--green-light);
  }
  .details {
    position: absolute;
    left: 376px;
    bottom: 52px;
    font-size: 15px;
    line-height: 1.45;
  }
  .services-title {
    font-weight: 700;
    font-size: 15px;
    color: var(--green-dark);
    text-transform: uppercase;
    letter-spacing: 0.5px;
  }
  .services-list { list-style: none; }
  .person {
    position: absolute;
    left: 52px;
    top: 150px;
  }
  .person-name {
    font-weight: 700;
    font-size: 17px;
    color: var(--green-dark);
    text-transform: uppercase;
    letter-spacing: 0.5px;
  }
  .person-role { font-size: 15px; line-height: 1.1; }
  .contact-list { list-style: none; }
  .contact-list li {
    display: flex;
    align-items: center;
    gap: 8px;
    font-size: 15px;
    line-height: 1.7;
  }
  .contact-list svg { width: 14px; height: 14px; fill: var(--green-dark); flex: none; }
</style>
</head>
<body>

  <section class="card card-front">
    <div class="brand">
      <span class="brand-mark"></span>
      <span class="brand-name">Timber Ridge Land Services</span>
    </div>
    <div class="divider"></div>
    <div class="details">
      <h2 class="services-title">Our Services</h2>
      <ul class="services-list">
        <li>Forestry Mulching For Land Clearing<br>And Vegetation Control</li>
        <li>Brush And Small Tree Removal</li>
        <li>Wildlife Habitat Improvement And Trail</li>
        <li>Property Access Creation</li>
      </ul>
    </div>
  </section>

  <section class="card card-back">
    <div class="person">
      <p class="person-name">Daniel Reyes</p>
      <p class="person-role">Founder</p>
    </div>
    <div class="brand">
      <span class="brand-mark"></span>
      <span class="brand-name">Timber Ridge Land Services</span>
    </div>
    <div class="divider"></div>
    <div class="details">
      <ul class="contact-list">
        <li>
          <svg viewBox="0 0 24 24" aria-hidden="true"><path d="M6.6 10.8a15.1 15.1 0 0 0 6.6 6.6l2.2-2.2a1 1 0 0 1 1-.25 11.4 11.4 0 0 0 3.6.57 1 1 0 0 1 1 1V20a1 1 0 0 1-1 1A17 17 0 0 1 3 4a1 1 0 0 1 1-1h3.5a1 1 0 0 1 1 1c0 1.25.2 2.45.57 3.6a1 1 0 0 1-.25 1z"/></svg>
          555-014-2290
        </li>
        <li>
          <svg viewBox="0 0 24 24" aria-hidden="true"><path d="M2 5h20v14H2z M4 7v.5l8 5 8-5V7l-8 5z" fill-rule="evenodd"/></svg>
          info@timberridgelandservices.com
        </li>
        <li>
          <svg viewBox="0 0 24 24" aria-hidden="true"><path d="M12 2a10 10 0 1 0 0 20 10 10 0 0 0 0-20zm0 2c.9 0 2.2 1.9 2.7 5H9.3C9.8 5.9 11.1 4 12 4zM4.3 11h3a17 17 0 0 0 .1 2h-3a8 8 0 0 1-.1-2zm5 0h5.4a15 15 0 0 1 0 2H9.3a15 15 0 0 1 0-2zm7.4 0h3a8 8 0 0 1 0 2h-3a17 17 0 0 0 0-2zM9.3 15h5.4c-.5 3.1-1.8 5-2.7 5s-2.2-1.9-2.7-5z"/></svg>
          www.timberridgelandservices.com
        </li>
        <li>
          <svg viewBox="0 0 24 24" aria-hidden="true"><path d="M12 2a7 7 0 0 0-7 7c0 5 7 13 7 13s7-8 7-13a7 7 0 0 0-7-7zm0 9.5A2.5 2.5 0 1 1 12 6.5a2.5 2.5 0 0 1 0 5z"/></svg>
          00 dummy city, dummy place 0000
        </li>
      </ul>
    </div>
  </section>

</body>
</html>
```